The Wardrobe Sage needs a business card

The wardrobe sage is a lead generation service serving the Custom Closet industry.

Here is the basic card information:

The Wardrobe Sage
Dorian Pettigrew
Owner/CEO
Charlotte, NC
704-318-5527 Cell
Email: dpettigrew@TheWardrobeSage.com

Additional information for the card:

"High quality, flat rate lead generation exclusively for the custom closet industry"

Bullet points for the back:

- Low fixed cost
- Easy to budget
- Guaranteed qualified Leeds
- Exclusivity per city

Logo attached, head shot attached. Photos of closet systems attached

```html
<!DOCTYPE html>
<html lang="en">
<head>
<meta charset="utf-8">
<title>The Wardrobe Sage – Business Card</title>
<link href="https://fonts.googleapis.com/css2?family=Playfair+Display:wght@500&family=Montserrat:wght@400;600&family=Oswald:wght@500&display=swap" rel="stylesheet">
<style>
  :root {
    --ink: #1c1c1c;
    --ink-soft: #262626;
    --copper: #b06f33;
    --copper-light: #c98a4b;
    --paper: #ffffff;
    --stage: #e9e7e4;
    --grey-tile: #cfcfcf;
    --text-dark: #222;
  }
  * { box-sizing: border-box; margin: 0; padding: 0; }
  html, body { width: 1200px; height: 1200px; overflow: hidden; background: var(--stage); }
  .sheet { position: relative; width: 1200px; height: 1200px; }
  .card {
    position: absolute; top: 200px; width: 460px; height: 800px;
    border-radius: 28px; overflow: hidden;
    box-shadow: 0 10px 30px rgba(0,0,0,.18);
  }
  /* Front */
  .card--front { left: 100px; background: linear-gradient(160deg, var(--ink-soft), var(--ink)); color: var(--paper); font-family: "Montserrat", sans-serif; text-align: center; }
  .brand { position: absolute; top: 95px; left: 0; right: 0; display: flex; align-items: center; justify-content: center; gap: 12px; }
  .brand__mark { width: 18px; height: 18px; border-radius: 50%; background: var(--copper); }
  .brand__name { font-family: "Playfair Display", serif; font-weight: 500; font-size: 38px; color: var(--paper); white-space: nowrap; }
  .portrait {
    position: absolute; top: 205px; left: 50%; transform: translateX(-50%);
    width: 225px; height: 225px; border-radius: 50%;
    border: 4px solid var(--copper);
    background: radial-gradient(circle at 50% 40%, #f2f2f2 0 45%, #dcdcdc 46%, #2f3a4d 70%);
  }
  .person__name { position: absolute; top: 470px; left: 0; right: 0; font-weight: 600; font-size: 31px; letter-spacing: 1px; color: var(--copper-light); white-space: nowrap; }
  .person__role { position: absolute; top: 512px; left: 0; right: 0; font-size: 17px; letter-spacing: .5px; }
  .contact-icons { position: absolute; top: 552px; left: 0; right: 0; display: flex; align-items: center; justify-content: center; gap: 14px; }
  .contact-icons .rule { width: 48px; height: 2px; background: var(--copper); }
  .contact-icons svg { width: 46px; height: 46px; }
  .contact-list { position: absolute; top: 622px; left: 0; right: 0; font-size: 19px; line-height: 1.45; }
  .contact-list .email { font-size: 16px; }
  .tagline {
    position: absolute; bottom: 0; left: 0; right: 0; height: 86px;
    background: var(--copper); display: flex; align-items: center; justify-content: center;
    font-weight: 600; font-size: 15px; line-height: 1.35; padding: 0 20px;
  }
  /* Back */
  .card--back { left: 640px; background: var(--paper); }
  .benefits { position: absolute; top: 70px; left: 40px; list-style: none; font-family: "Oswald", sans-serif; font-weight: 500; font-size: 24px; line-height: 1.32; color: var(--text-dark); text-transform: uppercase; }
  .benefits li::before { content: ""; display: inline-block; width: 8px; height: 8px; border-radius: 50%; background: var(--copper); margin-right: 10px; vertical-align: middle; }
  .gallery { position: absolute; top: 200px; left: 0; width: 460px; height: 300px; }
  .brand--back { top: auto; bottom: 120px; }
  .brand--back .brand__name { color: #5a5a5a; }
  .back-strip { position: absolute; bottom: 0; left: 0; right: 0; height: 16px; background: var(--copper); }
</style>
</head>
<body>
<main class="sheet">
  <section class="card card--front">
    <div class="brand"><span class="brand__mark"></span><span class="brand__name">The Wardrobe Sage</span></div>
    <div class="portrait" role="img" aria-label="Head shot of the owner"></div>
    <h1 class="person__name">DORIAN PETTIGREW</h1>
    <p class="person__role">OWNER | CEO</p>
    <div class="contact-icons">
      <span class="rule"></span>
      <svg viewBox="0 0 46 46" aria-hidden="true"><circle cx="23" cy="23" r="20" fill="none" stroke="var(--copper)" stroke-width="2.5"/><path d="M16 14c2-1 3 0 4 3s0 3-1 4c1 3 3 5 6 6 1-1 2-2 4-1s4 2 3 4-3 2-5 2c-7-1-12-7-13-13 0-2 1-4 2-5z" fill="var(--copper)"/></svg>
      <svg viewBox="0 0 46 46" aria-hidden="true"><circle cx="23" cy="23" r="20" fill="none" stroke="var(--copper)" stroke-width="2.5"/><rect x="12" y="15" width="22" height="16" rx="1.5" fill="var(--copper)"/><path d="M12 16l11 8 11-8" fill="none" stroke="var(--ink)" stroke-width="1.8"/></svg>
      <svg viewBox="0 0 46 46" aria-hidden="true"><circle cx="23" cy="23" r="20" fill="none" stroke="var(--copper)" stroke-width="2.5"/><path d="M23 12a7 7 0 0 1 7 7c0 5-7 14-7 14s-7-9-7-14a7 7 0 0 1 7-7z" fill="none" stroke="var(--copper)" stroke-width="2.5"/><circle cx="23" cy="19" r="2.5" fill="var(--copper)"/></svg>
      <span class="rule"></span>
    </div>
    <div class="contact-list">
      <p>704-318-5527</p>
      <p class="email">dpettigrew@TheWardrobeSage.com</p>
      <p>Larkfield NC</p>
    </div>
    <p class="tagline">High quality, flat rate lead generation<br>exclusively for the custom closet industry</p>
  </section>

  <section class="card card--back">
    <ul class="benefits">
      <li>Low fixed cost</li>
      <li>Easy to budget</li>
      <li>Guaranteed qualified leeds</li>
      <li>Exclusivity per city</li>
    </ul>
    <svg class="gallery" viewBox="0 0 460 300">
      <defs>
        <linearGradient id="wood" x1="0" y1="0" x2="1" y2="1"><stop offset="0" stop-color="#c99a6b"/><stop offset="1" stop-color="#e9e2d8"/></linearGradient>
        <linearGradient id="lounge" x1="0" y1="0" x2="1" y2="1"><stop offset="0" stop-color="#8a6a55"/><stop offset="1" stop-color="#d9c2a8"/></linearGradient>
        <linearGradient id="island" x1="0" y1="0" x2="1" y2="1"><stop offset="0" stop-color="#e8e2da"/><stop offset="1" stop-color="#2f4a7a"/></linearGradient>
      </defs>
      <polygon points="380,95 440,155 380,155" fill="var(--grey-tile)"/>
      <g transform="translate(270 95) rotate(45)">
        <rect x="-62" y="-62" width="124" height="124" fill="none" stroke="var(--copper)" stroke-width="2.5"/>
        <rect x="-55" y="-55" width="110" height="110" fill="url(#wood)" role="img" aria-label="Photo of a walk-in closet with wooden shelving"/>
      </g>
      <g transform="translate(176 189) rotate(45)">
        <rect x="-62" y="-62" width="124" height="124" fill="none" stroke="var(--copper)" stroke-width="2.5"/>
        <rect x="-55" y="-55" width="110" height="110" fill="url(#lounge)" role="img" aria-label="Photo of a dressing room with a lounge chair"/>
      </g>
      <g transform="translate(364 189) rotate(45)">
        <rect x="-62" y="-62" width="124" height="124" fill="none" stroke="var(--copper)" stroke-width="2.5"/>
        <rect x="-55" y="-55" width="110" height="110" fill="url(#island)" role="img" aria-label="Photo of a closet with a blue drawer island"/>
      </g>
    </svg>
    <div class="brand brand--back"><span class="brand__mark"></span><span class="brand__name">The Wardrobe Sage</span></div>
    <div class="back-strip"></div>
  </section>
</main>
</body>
</html>
```